Stationery design for software development / consultancy company

We need stationary design based on company logo.

We are based in London, UK and we are providing integration solutions development / consultancy services for VEQ integration projects across UK.

Our name refers two words - integration and grace - and it shows our clients our main specialization field and key characteristics of our solutions / products. We also would like to be associated with follow words: smart, reliable, unique.

Project delivery should include:
- Powerpoint template (needs to have a Cover Page, Table of Contents, 1-2 sample pages, and a Closing/Summary slide at the end)
- Letterhead A4 (Word template)
- Standard invoice A4 (Word template)
- With Compliments Slips A5 (Word template)
- Business card (adobe illustrator)

Attached is logo in vector (please use logo with white background!) and company details for printed stationery.

highly skilled IT professionals

Software

• Clear background in all A4/A5 documents.
All text should be editable, i.e. I will need sources.
• I would prefer light, web 2.0 style colours, follow are in my main interest:
- combination of light grey and orange
- Logo colours
• Please no watermarks on printed stationary

```html
<!DOCTYPE html>
<html lang="en">
<head>
<meta charset="utf-8">
<title>Corvane stationery</title>
<link href="https://fonts.googleapis.com/css2?family=Arimo:wght@400;700&display=swap" rel="stylesheet">
<style>
:root{
  --backdrop:#a3b9ba;
  --paper:#ffffff;
  --card-light:#eceeef;
  --card-dark:#1c1d1d;
  --ink:#222;
  --ink-soft:#555;
  --brand-grey:#4a4a4a;
  --orange:#f07f1e;
  --green:#8cba3f;
  --blue:#1f9bd7;
  --rule:#555;
  --ghost:#eef3f6;
}
*{box-sizing:border-box;margin:0;padding:0}
html,body{width:1200px;height:818px;overflow:hidden}
body{background:var(--backdrop);position:relative;font-family:"Arimo",Arial,sans-serif;color:var(--ink)}
.sheet{position:absolute;background:var(--paper);overflow:hidden}
.brand{position:absolute;display:flex;align-items:center;gap:5px;font-weight:700;color:var(--brand-grey);letter-spacing:-.02em}
.brand .dot{border-radius:50%;background:var(--orange);flex:none}
.stripe{position:absolute;left:0;right:0;height:2px;
  background:linear-gradient(90deg,var(--orange) 0 33.3%,var(--green) 33.3% 66.6%,var(--blue) 66.6% 100%)}
.ghost-mark{position:absolute;border-radius:50%;background:var(--ghost)}
.tiny{font-size:5.5px;line-height:1.3}

/* business cards */
.card-front{left:336px;top:62px;width:363px;height:217px;background:radial-gradient(circle at 40% 20%,#2c2d2d,var(--card-dark) 70%)}
.card-front .brand{left:68px;top:80px;font-size:44px;color:#fff;gap:10px}
.card-front .brand .dot{width:32px;height:32px}
.card-back{left:704px;top:62px;width:363px;height:217px;background:linear-gradient(160deg,#f3f4f5,var(--card-light))}
.card-back .brand{left:0;right:0;top:28px;flex-direction:column;font-size:36px;gap:6px}
.card-back .brand .dot{width:22px;height:22px}
.card-back .details{position:absolute;top:144px;left:20px;right:14px;display:flex;justify-content:space-between;font-size:9.5px;line-height:1.25;color:var(--ink-soft)}
.card-back .details b{color:var(--ink)}
.card-back .stripe{left:10px;right:10px;top:205px}

/* invoice */
.invoice{left:24px;top:326px;width:336px;height:448px}
.sheet .brand.small{left:26px;top:24px;font-size:13px}
.sheet .brand.small .dot{width:10px;height:10px}
.a4 .stripe{top:56px;height:1.5px}
.invoice .title{position:absolute;right:18px;top:24px;text-align:right}
.invoice .title h1{font-size:8px;font-weight:700;margin-bottom:3px}
.invoice .from{position:absolute;left:26px;top:76px}
.invoice .to{position:absolute;right:18px;top:76px;text-align:right}
.invoice .line{position:absolute;left:33px;width:279px;height:1px;background:var(--rule)}
.invoice .pay{position:absolute;left:220px;top:322px}
.invoice .regard{position:absolute;left:283px;top:346px}
.invoice .sign{position:absolute;left:288px;top:388px}
.footer-note{position:absolute;left:0;right:0;top:430px;text-align:center}
.a4 .ghost-mark{width:96px;height:96px;right:8px;top:340px}

/* letterhead */
.letterhead{left:381px;top:326px;width:335px;height:448px}
.letterhead .contact{position:absolute;left:192px;top:16px;display:flex;gap:12px}
.letterhead .brand.small{top:24px}

/* envelope */
.envelope{left:753px;top:326px;width:425px;height:197px}
.envelope svg.flap{position:absolute;left:0;top:0}
.envelope .brand{left:0;right:0;justify-content:center;top:26px;font-size:19px}
.envelope .brand .dot{width:14px;height:14px}
.envelope .contact{position:absolute;left:108px;top:178px;display:flex;gap:12px}
.envelope .stripe{top:190px}

/* compliments slip */
.slip{left:753px;top:564px;width:425px;height:195px}
.slip .brand{left:21px;top:24px;font-size:20px}
.slip .brand .dot{width:15px;height:15px}
.slip .ghost-mark{width:88px;height:88px;right:-10px;top:100px}
.slip .stripe{top:185px}
</style>
</head>
<body>

<section class="sheet card-front">
  <div class="brand"><span class="dot"></span>Corvane</div>
</section>

<section class="sheet card-back">
  <div class="brand"><span class="dot"></span>Corvane</div>
  <div class="details">
    <div><b>Daniel Royce</b><br>Director</div>
    <div><b>Corvane Limited</b><br>42 Mill Court<br>88 Lower Bridge Street<br>London, SE4 2QT<br>United Kingdom</div>
    <div><b>www.corvane.co.uk</b><br>daniel@corvane.co.uk<br>+44(0)121 000 4821<br>+44(0)7700900412</div>
  </div>
  <div class="stripe"></div>
</section>

<section class="sheet a4 invoice">
  <div class="brand small"><span class="dot"></span>Corvane</div>
  <div class="title tiny"><h1>Invoice</h1>Invoice no : 1025<br>invoice date : 8 may 2011</div>
  <div class="stripe"></div>
  <div class="from tiny"><b>Corvane Limited</b><br>42 Mill Court<br>88 Lower Bridge Street<br>London<br>SE4 2QT<br>United Kingdom</div>
  <div class="to tiny"><b>Sample client</b><br>42 Mill Court<br>88 Lower Bridge Street<br>London, SE4 2QT<br>United Kingdom</div>
  <div class="line" style="top:150px"></div>
  <div class="line" style="top:310px"></div>
  <div class="ghost-mark"></div>
  <div class="pay tiny">yours payment :</div>
  <div class="regard tiny">best regard</div>
  <div class="sign tiny">Martin P.</div>
  <div class="footer-note tiny">Company registration 7104382 (England and Wales Vat No 310 5582 07</div>
</section>

<section class="sheet a4 letterhead">
  <div class="brand small"><span class="dot"></span>Corvane</div>
  <div class="contact tiny">
    <div><b>Corvane Limited</b><br>42 Mill Court<br>88 Lower Bridge Street<br>London, SE4 2QT<br>United Kingdom</div>
    <div><b>www.corvane.co.uk</b><br>daniel@corvane.co.uk<br>+44(0)121 000 4821<br>+44(0)7700900412</div>
  </div>
  <div class="stripe"></div>
  <div class="ghost-mark"></div>
  <div class="footer-note tiny">Company registration 7104382 (England and Wales Vat No 310 5582 07</div>
</section>

<section class="sheet envelope">
  <svg class="flap" width="425" height="80" viewBox="0 0 425 80" aria-hidden="true">
    <path d="M0 5 Q10 20 40 30 L205 70 Q212 72 220 70 L385 30 Q415 20 425 0" fill="none" stroke="#999" stroke-width="0.8"/>
  </svg>
  <div class="brand"><span class="dot"></span>Corvane</div>
  <div class="contact tiny">
    <span>w : www.corvane.co.uk</span><span>e : daniel@corvane.co.uk</span><span>T : +44(0)121 000 4821</span><span>M : +44(0)7700900412</span>
  </div>
  <div class="stripe"></div>
</section>

<section class="sheet slip">
  <div class="brand"><span class="dot"></span>Corvane</div>
  <div class="ghost-mark"></div>
  <div class="stripe"></div>
</section>

</body>
</html>
```